Book Cover Design 'Boundless Tide - Lessons In Inner Sovereignty'

I need to see pitches / artwork for a book cover for new book designed to start a new global spiritual movement and save humanity. The book merges science and spirituality and explains to the reader why they are an all powerful god.

```html
<!DOCTYPE html>
<html lang="en">
<head>
<meta charset="utf-8">
<title>Boundless Tide – Lessons In Inner Sovereignty – Cover Wrap</title>
<link href="https://fonts.googleapis.com/css2?family=Oswald:wght@600;700&family=Roboto:wght@300;400&display=swap" rel="stylesheet">
<style>
  :root {
    --stage: #6e6e6e;
    --night: #050914;
    --deep-navy: #0b1628;
    --nebula-blue: #2b4a6a;
    --nebula-warm: #b4552a;
    --gold-glow: #e7b46a;
    --silver-light: #f2f5f8;
    --silver-mid: #a9b6c4;
    --silver-dark: #6f7d8c;
    --ink-light: #e6e9ee;
    --accent-orange: #e39a3a;
    --placeholder: #ffffff;
    --fold-line: rgba(255,255,255,0.12);
  }
  html, body {
    margin: 0;
    padding: 0;
    width: 1200px;
    height: 2182px;
    overflow: hidden;
    background: var(--stage);
  }
  .cover-wrap {
    position: absolute;
    left: 40px;
    top: 703px;
    width: 1120px;
    height: 776px;
    background: var(--night);
    box-shadow: 0 10px 24px rgba(0,0,0,0.45);
    overflow: hidden;
    font-family: "Roboto", Arial, sans-serif;
    color: var(--ink-light);
  }
  .panel { position: absolute; top: 0; height: 776px; }
  .back-cover { left: 0; width: 512px; }
  .spine { left: 512px; width: 97px; border-left: 1px solid var(--fold-line); border-right: 1px solid var(--fold-line); box-sizing: border-box; }
  .front-cover { left: 609px; width: 511px; }

  .starfield {
    position: absolute; inset: 0;
    background:
      radial-gradient(ellipse 60% 40% at 30% 35%, rgba(60,95,130,0.55), transparent 70%),
      radial-gradient(ellipse 50% 30% at 75% 20%, rgba(90,110,140,0.35), transparent 70%),
      linear-gradient(180deg, var(--nebula-blue) 0%, var(--deep-navy) 45%, var(--night) 100%);
  }
  .spine .starfield {
    background:
      radial-gradient(ellipse 80% 30% at 50% 20%, rgba(60,95,130,0.45), transparent 70%),
      linear-gradient(180deg, var(--nebula-blue) 0%, var(--deep-navy) 50%, var(--night) 100%);
  }
  .hero-art {
    position: absolute; inset: 0;
    background:
      radial-gradient(circle at 58% 22%, rgba(231,180,106,0.55), transparent 32%),
      radial-gradient(circle at 80% 18%, rgba(180,85,42,0.55), transparent 30%),
      radial-gradient(ellipse 55% 40% at 50% 45%, rgba(70,110,160,0.55), transparent 70%),
      radial-gradient(circle at 72% 55%, rgba(160,110,50,0.35), transparent 35%),
      linear-gradient(180deg, #1c2c46 0%, #101c33 55%, var(--night) 85%);
  }

  .title-art { position: absolute; display: block; }
  .back-title { left: 140px; top: 120px; width: 240px; height: 110px; }
  .front-title { left: 60px; top: 495px; width: 392px; height: 190px; }

  .subtitle {
    position: absolute; margin: 0; text-align: center;
    font-weight: 300; color: var(--ink-light);
  }
  .back-subtitle { left: 0; width: 520px; top: 240px; font-size: 17px; }
  .front-subtitle { left: 0; width: 511px; top: 690px; font-size: 27px; }

  .blurb {
    position: absolute; left: 64px; top: 268px; width: 384px;
    margin: 0; font-size: 9.6px; line-height: 13.6px; text-align: justify;
    color: var(--ink-light);
  }
  .blurb p { margin: 0; }

  .author-heading {
    position: absolute; left: 0; width: 512px; top: 484px; margin: 0;
    text-align: center; font-size: 17px; font-weight: 300; color: var(--accent-orange);
  }
  .author-photo {
    position: absolute; left: 64px; top: 508px; width: 109px; height: 139px;
    background: var(--placeholder);
  }
  .author-bio {
    position: absolute; left: 184px; top: 508px; width: 264px; margin: 0;
    font-size: 9.6px; line-height: 13.6px; text-align: justify; color: var(--ink-light);
  }

  .spine-title, .spine-author {
    position: absolute; left: 50%; margin: 0; white-space: nowrap;
    transform-origin: center; color: var(--ink-light);
  }
  .spine-title {
    top: 225px; font-family: "Oswald", "Arial Narrow", sans-serif; font-weight: 700;
    font-size: 34px; letter-spacing: 0.5px;
    transform: translate(-50%, -50%) rotate(90deg);
  }
  .spine-author {
    top: 623px; font-size: 24px; font-weight: 300;
    transform: translate(-50%, -50%) rotate(90deg);
  }
</style>
</head>
<body>
  <main class="cover-wrap">

    <section class="panel back-cover">
      <div class="starfield" role="img" aria-label="Deep space nebula with faint star clusters and scattered handwritten equations"></div>

      <svg class="title-art back-title" viewBox="0 0 240 110" aria-label="Boundless Tide">
        <defs>
          <linearGradient id="silver-back" x1="0" y1="0" x2="0" y2="1">
            <stop offset="0" stop-color="var(--silver-light)"/>
            <stop offset="0.5" stop-color="var(--silver-mid)"/>
            <stop offset="1" stop-color="var(--silver-light)"/>
          </linearGradient>
        </defs>
        <text x="120" y="50" text-anchor="middle" textLength="224" lengthAdjust="spacingAndGlyphs"
              font-family="Oswald, sans-serif" font-weight="700" font-size="58" fill="url(#silver-back)">BOUNDLESS</text>
        <text x="120" y="106" text-anchor="middle" textLength="224" lengthAdjust="spacing"
              font-family="Oswald, sans-serif" font-weight="700" font-size="58" fill="url(#silver-back)">TIDE</text>
      </svg>

      <p class="subtitle back-subtitle">Lessons In Inner Sovereignty</p>

      <div class="blurb">
        <p>Lorem Ipsum is simply dummy text of the printing and typesetting industry. Lorem Ipsum has been the industry's standard dummy text ever since the 1500s, when an unknown printer took a galley of type and scrambled it to make a type specimen book. It has survived not only five centuries, but also the leap into electronic typesetting, remaining essentially unchanged. It was popularised in the 1960s with the release of Tessaline sheets containing Lorem Ipsum passages, and more recently with desktop publishing software like Folio Layout including versions of Lorem Ipsum.</p>
        <p>Lorem Ipsum is simply dummy text of the printing and typesetting industry. Lorem Ipsum has been the industry's standard dummy text ever since the 1500s, when an unknown printer took a galley of type and scrambled it to make a type specimen book. It has survived not only five centuries, but also the leap into electronic typesetting, remaining essentially unchanged. It was popularised in the 1960s with the release of Tessaline sheets containing Lorem Ipsum passages, and more recently with desktop publishing software like Folio Layout including versions of Lorem</p>
      </div>

      <h3 class="author-heading">AUTHOR NAME</h3>
      <div class="author-photo" role="img" aria-label="Author portrait placeholder"></div>
      <p class="author-bio">Lorem Ipsum is simply dummy text of the printing and typesetting industry. Lorem Ipsum has been the industry's standard dummy text ever since the 1500s, when an unknown printer took a galley of type and scrambled it to make a type specimen book. It has survived not only five centuries, but also the leap into electronic typesetting, remaining essentially unchanged. It was popularised in the 1960s with the release of Tessaline sheets containing Lorem Ipsum passages, and more recently with desktop publishing software like Folio Layout including versions of Lorem Ipsum.</p>
    </section>

    <section class="panel spine">
      <div class="starfield" role="img" aria-label="Continuation of the deep space nebula"></div>
      <h2 class="spine-title">BOUNDLESS TIDE</h2>
      <p class="spine-author">AUTHOR NAME</p>
    </section>

    <section class="panel front-cover">
      <div class="hero-art" role="img" aria-label="Cosmic illustration of a glowing human profile dissolving into nebula light, with a golden astronomical dial of symbols behind it"></div>

      <svg class="title-art front-title" viewBox="0 0 392 190" aria-label="Boundless Tide">
        <defs>
          <linearGradient id="silver-front" x1="0" y1="0" x2="0" y2="1">
            <stop offset="0" stop-color="var(--silver-light)"/>
            <stop offset="0.45" stop-color="var(--silver-mid)"/>
            <stop offset="0.6" stop-color="var(--silver-dark)"/>
            <stop offset="1" stop-color="var(--silver-light)"/>
          </linearGradient>
        </defs>
        <text x="196" y="90" text-anchor="middle" textLength="386" lengthAdjust="spacingAndGlyphs"
              font-family="Oswald, sans-serif" font-weight="700" font-size="108" fill="url(#silver-front)">BOUNDLESS</text>
        <text x="196" y="186" text-anchor="middle" textLength="386" lengthAdjust="spacing"
              font-family="Oswald, sans-serif" font-weight="700" font-size="96" fill="url(#silver-front)">TIDE</text>
      </svg>

      <p class="subtitle front-subtitle">Lessons In Inner Sovereignty</p>
    </section>

  </main>
</body>
</html>
```